Construction Company's Job Site Signage City ordinance job signage for brand awareness.

We are looking for something with movement or texture (ei. water or something like that) and dislikes a white background. We are a company specializing in remedial construction, mold removal, and restoration. The concept is for 12” x 18” jobsite signs so they must be easy to read from a passing car as well. Please let me know if there is anything I can do to help or if it’s easier for me to submit. The CGC Number must be at least 1 inch lettering. www.TrevendCompanies.com

Target Market(s)

Upscale, high end estate neighborhoods at job sites which we are working on.

Industry/Entity Type

Construction

Colors
33b8a4
00a990
0892cd
0255a3
9bcb3c
add136
fbed22
fbee3e
fbf289

Requirements
Must have
• All text present in the current files.

```html
<!DOCTYPE html>
<html lang="en">
<head>
<meta charset="utf-8">
<title>Trevend Job Site Sign</title>
<link rel="stylesheet" href="https://fonts.googleapis.com/css2?family=Roboto+Condensed:wght@700&family=Open+Sans:wght@400&display=swap">
<style>
  :root {
    --canvas: #ffffff;
    --deep-green: #006b45;
    --teal: #33b8a4;
    --sea: #00a990;
    --sky: #0892cd;
    --navy: #0255a3;
    --lime: #9bcb3c;
    --leaf: #add136;
    --sun: #fbed22;
    --pale-sun: #fbf289;
    --band: #ffffff;
    --ink: #000000;
    --badge: #7fb89c;
    --badge-ink: #111111;
  }
  html, body {
    margin: 0;
    padding: 0;
    width: 1200px;
    height: 1000px;
    overflow: hidden;
    background: var(--canvas);
  }
  .sign {
    position: absolute;
    left: 38px;
    top: 125px;
    width: 1124px;
    height: 747px;
    box-shadow: 6px 8px 8px rgba(0,0,0,0.35);
    overflow: hidden;
  }
  .sign svg { display: block; }
  .headline {
    font-family: "Roboto Condensed", "Arial Narrow", sans-serif;
    font-weight: 700;
    fill: var(--ink);
  }
  .brand-name {
    font-family: "Roboto Condensed", "Arial Narrow", sans-serif;
    font-weight: 700;
    fill: var(--deep-green);
  }
  .contact {
    font-family: "Open Sans", Arial, sans-serif;
    font-weight: 400;
    fill: var(--badge-ink);
  }
</style>
</head>
<body>
  <div class="sign">
    <svg width="1124" height="747" viewBox="0 0 1124 747">
      <defs>
        <linearGradient id="texture-tones" x1="0" y1="0" x2="1" y2="1">
          <stop offset="0" stop-color="#1f9a7a"/>
          <stop offset="0.3" stop-color="#0c6f86"/>
          <stop offset="0.55" stop-color="#2fa77a"/>
          <stop offset="0.75" stop-color="#8fc446"/>
          <stop offset="1" stop-color="#2a9e86"/>
        </linearGradient>
      </defs>

      <rect class="texture-field" role="img" aria-label="Geometric triangle pattern in greens, teals, blues and yellows" x="0" y="0" width="1124" height="747" fill="url(#texture-tones)"/>

      <polygon class="message-band" points="0,257 1124,23 1124,345 0,583" fill="var(--band)"/>

      <g class="message">
        <text class="headline" transform="translate(234 290) rotate(-12)" x="0" y="0" font-size="86" textLength="634" lengthAdjust="spacingAndGlyphs">BULDING SOLUTIONS</text>
        <text class="headline" transform="translate(80 423) rotate(-12)" x="0" y="0" font-size="86" textLength="994" lengthAdjust="spacingAndGlyphs">AROUND COMPLEX STRUCTURES</text>
        <text class="headline" transform="translate(110 515) rotate(-12)" x="0" y="0" font-size="86" textLength="963" lengthAdjust="spacingAndGlyphs">(239) 555-0148 . CGC 1029384</text>
      </g>

      <g class="badge">
        <circle cx="899" cy="565" r="170" fill="var(--badge)"/>
        <text class="brand-name" x="899" y="530" font-size="62" text-anchor="middle">Trevend</text>
        <text class="contact" x="899" y="591" font-size="18" text-anchor="middle">www.TrevendCompanies.com</text>
        <text class="contact" x="899" y="643" font-size="18" text-anchor="middle">800.555.0172</text>
      </g>
    </svg>
  </div>
</body>
</html>
```